Bref créative
Brivona Real Estate
Professional
Tom Radcliffe
President
782 W. Hollow Pine Rd. Suite 310
Crestmoor Heights, CA 90455
tom@BrivonaRealEstate.example
www.BrivonaRealEstate.example
I will upload our logo. If there is a problem with that please use logo on web site www.brivonarealestate.example
Please use our logo.

```html
<!DOCTYPE html>
<html lang="en">
<head>
<meta charset="utf-8">
<title>Brivona Real Estate – Business Card</title>
<link href="https://fonts.googleapis.com/css2?family=Arimo:wght@400;700&display=swap" rel="stylesheet">
<style>
  :root {
    --navy-deep: #24405f;
    --navy-mid: #34557c;
    --navy-light: #4a6d96;
    --paper: #ffffff;
    --brand-ink: #1f3554;
    --tagline: #5b6b7e;
    --contact-text: #ffffff;
  }
  * { box-sizing: border-box; margin: 0; padding: 0; }
  html, body {
    width: 1200px; height: 336px; overflow: hidden;
    background: var(--paper);
    font-family: "Arimo", Arial, sans-serif;
  }
  .sheet { position: relative; width: 1200px; height: 336px; }
  .card {
    position: absolute; top: 0; width: 588px; height: 336px; overflow: hidden;
    background: radial-gradient(circle at 80% 40%, var(--navy-light) 0%, var(--navy-mid) 45%, var(--navy-deep) 100%);
  }
  .card--front { left: 0; }
  .card--back { left: 612px; }
  .card__sweep { position: absolute; inset: 0; width: 100%; height: 100%; }
  .brand {
    position: absolute; left: 34px; top: 192px;
    display: flex; flex-direction: column; color: var(--brand-ink);
  }
  .brand__row { display: flex; align-items: center; gap: 10px; }
  .brand__mark { width: 30px; height: 30px; background: var(--navy-mid); }
  .brand__name { font-weight: 700; font-size: 38px; letter-spacing: 2px; line-height: 1; }
  .brand__sub { font-weight: 700; font-size: 15px; letter-spacing: 7px; margin: 4px 0 0 40px; }
  .brand__tagline { font-size: 11.5px; letter-spacing: 0.6px; color: var(--tagline); margin-top: 8px; }
  .holder { position: absolute; left: 350px; top: 14px; color: var(--contact-text); }
  .holder__name { font-size: 20px; font-weight: 700; }
  .holder__title { font-size: 13px; margin-top: 4px; }
  .contact {
    position: absolute; left: 350px; top: 182px; list-style: none;
    color: var(--contact-text); font-size: 11.5px; line-height: 19px;
    white-space: nowrap;
  }
</style>
</head>
<body>
<div class="sheet">
  <section class="card card--front">
    <svg class="card__sweep" viewBox="0 0 588 336" aria-hidden="true">
      <path d="M0 40 C130 40 310 150 340 336 L0 336 Z" fill="#ffffff"/>
    </svg>
    <div class="holder">
      <p class="holder__name">Tom Radcliffe</p>
      <p class="holder__title">President</p>
    </div>
    <div class="brand">
      <div class="brand__row"><span class="brand__mark"></span><span class="brand__name">BRIVONA</span></div>
      <span class="brand__sub">REAL ESTATE</span>
      <span class="brand__tagline">Buying • Selling • Leasing</span>
    </div>
    <ul class="contact">
      <li>782 W. Hollow Pine Rd. Suite 310</li>
      <li>Crestmoor Heights, CA 90455</li>
      <li>Phone : 310-555-0142</li>
      <li>Cell : 310-555-0187</li>
      <li>Fax : 888-555-0163</li>
      <li>Email : tom@BrivonaRealEstate.example</li>
      <li>Web : www.BrivonaRealEstate.example</li>
    </ul>
  </section>

  <section class="card card--back">
    <svg class="card__sweep" viewBox="0 0 588 336" aria-hidden="true">
      <path d="M0 40 C150 40 340 150 370 336 L0 336 Z" fill="#ffffff"/>
    </svg>
    <div class="brand">
      <div class="brand__row"><span class="brand__mark"></span><span class="brand__name">BRIVONA</span></div>
      <span class="brand__sub">REAL ESTATE</span>
      <span class="brand__tagline">Buying • Selling • Leasing</span>
    </div>
  </section>
</div>
</body>
</html>
```